self-employed education content specialist/consultant needs business card and logo design

I need a design for a double-sided business card (and logo) for my nascent consultancy business based in London UK, to hand out at a London trade show in a couple of weeks. The business simply has my name, "Marcus Tenwold".

I describe my service as a "content and engagement consultant". In essence I cover 2 areas:
- Advice to organisations on effective strategies and tactics for creating and distributing large volumes of media-rich content (video and interactive) for learning, training and professional development, that successfully engages and impacts on students and their teachers.
- Advice on growing and maintaining customer/end-user engagement to help maximise the reach and usage of this content.

I have uploaded a weighted list of key words that offer I hope a good feel of "the brand".

In terms of design I have put together a very rough initial idea for the card (see attached doc), which gives an idea of the key messages in text, but I feel it is not working visually, and looks too amateur. In particular I think the background/visuals of the info side needs work; the word cloud on the back of the card is perhaps rather "passé" and could be improved on; there is no "logo" at present; and I think overall it's not very "creative", i.e. it doesn't "stand out".

I am not set on font or background colours/design. The font itself should not be too businessy or too "comic sans", hence I've currently gone for something like Odile or Playfair Display.

Also note that
1. given budget and time constraints, I'm looking for designs for printing on paper, and to be of a fairly standard business card shape/size.
2. I have no web address at present, but will need a card design that can cope with this being added at a later date.

Overall I am hoping for something fairly clean, simple and clear, that will impress and speak to senior managers/business owners working in the education and edtech sectors.

As a self-employed consultant my budget is limited, so I don't expect the world for what I can offer, but am hoping that there are design experts out there who can swiftly interpret my brief and produce something suitable for my needs.

Target Market(s)

senior managers/business owners working in the education and edtech sectors.

Contact Information for Business Card

marcus tenwold
content and engagement consultant
education - training - development
+44 (0) 7731 482905
marcus.tenwold@quorvane.com

Font styles to use
Other font styles liked:
• Odile or Playfair Display are my favourites for now.

Colors

Designer to choose colors to be used in the design.

```html
<!DOCTYPE html>
<html lang="en">
<head>
<meta charset="utf-8">
<title>Marcus Tenwold – Business Card</title>
<link rel="stylesheet" href="https://fonts.googleapis.com/css2?family=Lato:wght@400;700&display=swap">
<style>
  :root {
    --backdrop: #3a3430;
    --card-black: #0d0d0e;
    --card-edge: #1a1a1c;
    --brand-blue: #1f5fa3;
    --text-light: #e4e4e6;
    --divider: #2c2c30;
    --silver: #d6d6d8;
    --pattern-dark: #151517;
    --pattern-mid: #232326;
  }
  * { box-sizing: border-box; margin: 0; padding: 0; }
  html, body {
    width: 1200px;
    height: 844px;
    overflow: hidden;
    background: var(--backdrop);
    font-family: "Lato", Arial, sans-serif;
  }
  .canvas {
    position: relative;
    width: 1200px;
    height: 844px;
  }
  .card {
    position: absolute;
    top: 277px;
    width: 500px;
    height: 290px;
    background: var(--card-black);
    border: 1px solid var(--card-edge);
    box-shadow: 0 10px 30px rgba(0, 0, 0, 0.45);
    overflow: hidden;
  }
  .card--front { left: 60px; }
  .card--back { left: 640px; }

  /* Front side */
  .front__identity {
    position: absolute;
    left: 28px;
    top: 0;
    width: 200px;
    height: 100%;
    display: flex;
    align-items: center;
    justify-content: center;
    gap: 10px;
  }
  .identity-dot {
    width: 16px;
    height: 16px;
    border-radius: 50%;
    background: var(--brand-blue);
    flex-shrink: 0;
  }
  .identity-name {
    color: var(--brand-blue);
    font-size: 22px;
    font-weight: 400;
    letter-spacing: 0.3px;
    white-space: nowrap;
  }
  .front__divider {
    position: absolute;
    left: 240px;
    top: 40px;
    width: 1px;
    height: 210px;
    background: var(--divider);
  }
  .front__details {
    position: absolute;
    left: 258px;
    top: 82px;
    right: 14px;
    color: var(--text-light);
  }
  .details-name {
    color: var(--brand-blue);
    font-size: 17px;
    font-weight: 700;
    letter-spacing: 0.5px;
    text-transform: uppercase;
    line-height: 1.1;
  }
  .details-role,
  .details-areas {
    font-size: 12.5px;
    line-height: 1.35;
  }
  .details-contact {
    list-style: none;
    margin-top: 18px;
  }
  .contact-item {
    display: flex;
    align-items: center;
    gap: 7px;
    font-size: 12.5px;
    line-height: 1.7;
  }
  .contact-icon {
    width: 11px;
    height: 11px;
    fill: var(--brand-blue);
    flex-shrink: 0;
  }

  /* Back side */
  .back__pattern {
    position: absolute;
    inset: 0;
    background: linear-gradient(135deg, var(--pattern-dark) 0%, var(--pattern-mid) 50%, var(--pattern-dark) 100%);
  }
  .back__identity {
    position: absolute;
    inset: 0;
    display: flex;
    align-items: center;
    justify-content: center;
    gap: 12px;
  }
  .back__identity .identity-dot {
    width: 20px;
    height: 20px;
    background: var(--silver);
  }
  .back__identity .identity-name {
    color: var(--silver);
    font-size: 28px;
  }
</style>
</head>
<body>
<main class="canvas">

  <section class="card card--front" aria-label="Business card, information side">
    <div class="front__identity">
      <span class="identity-dot"></span>
      <span class="identity-name">marcus tenwold</span>
    </div>
    <div class="front__divider"></div>
    <div class="front__details">
      <p class="details-name">Marcus Tenwold</p>
      <p class="details-role">content and engagement consultant</p>
      <p class="details-areas">education - training - development</p>
      <ul class="details-contact">
        <li class="contact-item">
          <svg class="contact-icon" viewBox="0 0 16 16" aria-hidden="true">
            <path d="M3.6 1.2 6 3.6c.4.4.4 1 0 1.4L4.9 6.1c.8 1.8 2.2 3.2 4 4l1.1-1.1c.4-.4 1-.4 1.4 0l2.4 2.4c.4.4.4 1 0 1.4l-1.3 1.3c-.6.6-1.5.8-2.3.5C6.6 13.2 2.8 9.4 1.4 5.8c-.3-.8-.1-1.7.5-2.3L3.2 1.2c.1-.1.3-.1.4 0z"/>
          </svg>
          <span>+44 (0) 7731 482905</span>
        </li>
        <li class="contact-item">
          <svg class="contact-icon" viewBox="0 0 16 16" aria-hidden="true">
            <path d="M1 3h14v1.2L8 8.6 1 4.2z"/>
            <path d="M1 5.6 8 10l7-4.4V13H1z"/>
          </svg>
          <span>marcus.tenwold@quorvane.com</span>
        </li>
      </ul>
    </div>
  </section>

  <section class="card card--back" aria-label="Business card, brand side">
    <div class="back__pattern" role="img" aria-label="Faint diagonal word pattern of brand keywords such as creative, editorial, project and engagement"></div>
    <div class="back__identity">
      <span class="identity-dot"></span>
      <span class="identity-name">marcus tenwold</span>
    </div>
  </section>

</main>
</body>
</html>
```